Business Image

I have recently had a new company logo made up and require some new business cards to go with it.

Target Market(s)

Developers & high worth clients.

Industry/Entity Type

Business

Contact Information for Business Card

The business is in the construction/management industry. It needs to be classy but have a industrial feel. I would like the business card to be a elegant presentation in itself.

Requirements
Must have
• Current logo & company name. Colouring needs to be the same as the current design also.
Nice to have
• A few different designs & presentations of single and double sided business cards.

```html
<!DOCTYPE html>
<html lang="en">
<head>
<meta charset="utf-8">
<title>Ridgeline Management Group – Business Cards</title>
<link rel="stylesheet" href="https://fonts.googleapis.com/css2?family=Open+Sans:wght@400;600&family=Tinos:wght@700&display=swap">
<style>
  :root {
    --bg: #a4a4a4;
    --card: #ffffff;
    --brand-blue: #4a8bcb;
    --mark-slate: #5f7487;
    --ink: #2f2f2f;
    --on-blue: #ffffff;
  }
  * { box-sizing: border-box; margin: 0; padding: 0; }
  html, body { width: 1200px; height: 1000px; overflow: hidden; }
  body {
    background: var(--bg);
    font-family: "Open Sans", Arial, sans-serif;
    position: relative;
  }
  .card {
    position: absolute;
    left: 220px;
    width: 760px;
    height: 420px;
    background: var(--card);
    box-shadow: 0 10px 24px rgba(0,0,0,0.18);
  }
  .card--front { top: 60px; }
  .card--back { top: 520px; }

  .card__frame {
    position: absolute;
    inset: 14px;
    border: 3px solid var(--brand-blue);
  }

  /* Front face */
  .front__band {
    position: absolute;
    left: 14px; top: 14px; bottom: 14px;
    width: 330px;
    background: var(--brand-blue);
    display: flex;
    flex-direction: column;
    justify-content: flex-end;
    padding: 0 0 56px 34px;
  }
  .company-name {
    font-family: "Tinos", "Times New Roman", serif;
    font-weight: 700;
    line-height: 1;
  }
  .front__band .company-name { color: var(--on-blue); font-size: 34px; letter-spacing: 1px; }
  .front__band .company-name span { display: block; font-size: 17px; letter-spacing: 2px; margin-top: 6px; }

  .front__identity {
    position: absolute;
    left: 344px; right: 14px; top: 14px; bottom: 14px;
    display: flex;
    flex-direction: column;
    align-items: center;
    justify-content: center;
    gap: 26px;
  }
  .brand-square {
    width: 120px; height: 120px;
    background: var(--mark-slate);
  }
  .front__email { color: var(--brand-blue); font-size: 15px; letter-spacing: 0.3px; }

  /* Back face */
  .back__identity {
    position: absolute;
    left: 14px; top: 14px; bottom: 14px;
    width: 250px;
    display: flex;
    flex-direction: column;
    align-items: center;
    justify-content: center;
    gap: 22px;
  }
  .back__identity .brand-square { width: 110px; height: 110px; }
  .back__identity .company-name { color: var(--brand-blue); font-size: 30px; text-align: center; }
  .back__identity .company-name span { display: block; font-size: 14px; letter-spacing: 1.5px; margin-top: 6px; }

  .back__panel {
    position: absolute;
    left: 264px; right: 14px; top: 14px; bottom: 14px;
    background: var(--brand-blue);
    padding: 12px;
  }
  .back__panel-frame {
    width: 100%; height: 100%;
    border: 2px solid var(--on-blue);
    display: flex;
    flex-direction: column;
    justify-content: center;
    gap: 30px;
    padding: 0 34px;
  }
  .contact-row {
    display: flex;
    justify-content: flex-end;
    align-items: center;
    gap: 22px;
    color: var(--on-blue);
    font-size: 19px;
    letter-spacing: 0.4px;
  }
  .contact-row svg { width: 26px; height: 26px; flex: none; }
</style>
</head>
<body>

<section class="card card--front" aria-label="Business card front">
  <div class="card__frame"></div>
  <div class="front__band">
    <p class="company-name">RIDGELINE<span>MANAGEMENT GROUP</span></p>
  </div>
  <div class="front__identity">
    <div class="brand-square" aria-hidden="true"></div>
    <p class="front__email">jordan@ridgelinegroup.com</p>
  </div>
</section>

<section class="card card--back" aria-label="Business card back">
  <div class="card__frame"></div>
  <div class="back__identity">
    <div class="brand-square" aria-hidden="true"></div>
    <p class="company-name">RIDGELINE<span>MANAGEMENT GROUP</span></p>
  </div>
  <div class="back__panel">
    <div class="back__panel-frame">
      <div class="contact-row">
        <span>1 (555) 014-2210</span>
        <svg viewBox="0 0 26 26" aria-hidden="true"><rect x="1" y="1" width="24" height="24" fill="none" stroke="#fff" stroke-width="1.5"/><rect x="9" y="6" width="8" height="14" rx="1" fill="none" stroke="#fff" stroke-width="1.5"/></svg>
      </div>
      <div class="contact-row">
        <span>1 (555) 014-2288</span>
        <svg viewBox="0 0 26 26" aria-hidden="true"><rect x="1" y="1" width="24" height="24" fill="none" stroke="#fff" stroke-width="1.5"/><path d="M8 6c-2 2-1 6 3 10s8 5 10 3l-3-3-2 1c-2-1-4-3-5-5l1-2z" fill="#fff"/></svg>
      </div>
      <div class="contact-row">
        <span>48 Harbor Row, Fairview, NY 10020, USA</span>
        <svg viewBox="0 0 26 26" aria-hidden="true"><rect x="1" y="1" width="24" height="24" fill="none" stroke="#fff" stroke-width="1.5"/><path d="M13 5a5 5 0 0 0-5 5c0 4 5 10 5 10s5-6 5-10a5 5 0 0 0-5-5z" fill="#fff"/><circle cx="13" cy="10" r="2" fill="#4a8bcb"/></svg>
      </div>
      <div class="contact-row">
        <span>jordan@ridgelinegroup.com</span>
        <svg viewBox="0 0 26 26" aria-hidden="true"><rect x="1" y="1" width="24" height="24" fill="none" stroke="#fff" stroke-width="1.5"/><rect x="6" y="8" width="14" height="10" fill="none" stroke="#fff" stroke-width="1.5"/><path d="M6 8l7 6 7-6" fill="none" stroke="#fff" stroke-width="1.5"/></svg>
      </div>
    </div>
  </div>
</section>

</body>
</html>
```